DUN Meridian Safeguard Sell Sheet

We need a two-sided portrait-style sell sheet for a new insurance product called the DUN Meridian Safeguard. The DUN Meridian Safeguard is a custom Executive Risk commercial insurance policy that provides the broadest level of protection available in the marketplace. The sell sheet would primarily use the colors blue, gray and white, have clean lines, minimal graphics (perhaps a picture of an executive boardroom at the top), three boxes (or text areas) to provide a brief description of the specific insurance products provided by the Meridian (Directors & Officers Liability, Employment Practices Liability, and Fiduciary Liability), be easy to read and really pique the reader's interest to learn more about the product. The title (DUN Meridian Safeguard) would overlay the graphic at the top, and just below the title would be the phrase "Expect More", which is our tagline for the product. There would be a two-sentence lead-in phrase just below the graphic ("Meridian Safeguard is an exclusive, custom-designed insurance policy tailored to a company’s specific risk profile. The policy was created to provide clients with a premium, industry-leading level of protection not found in the standard insurance marketplace". There needs to be another text section entitled "Return on Investment" and capable of containing three medium length sentences. There needs to be an "About Us" section (three to four medium-length sentences) and a "Contact Us" section (contact name, phone (x2), e-mail, address). On the back we want to discuss the specific features of the product by section of the policy (General Terms and Conditions, Directors & Officers Liability Insurance, Employment Practices Liability Insurance, Fiduciary Liability Insurance. This would likely be set out in bullet format.

I have attached a few examples found on the web that are similar to my vision for this sell sheet, but none that exactly fit our needs (whether graphically or due to specific layout).

Insurance

Serif

• I have uploaded a sample done in powerpoint. Please disregard the coloring as I did not have time to choose colors. I did not add the "About Us" and "Contact Us" sections on the front page and would like creative ideas on structuring that. On the back page, I think a nice looking table broken down by section of the policy would look nice, and allow us to enter bulleted coverage features for each section. Both graphics in the sample were found on google without watermarks by searching "board room" and "business agreement", respectively.

```html
<!DOCTYPE html>
<html lang="en">
<head>
<meta charset="utf-8">
<title>DUN Meridian Safeguard Sell Sheet</title>
<link href="https://fonts.googleapis.com/css2?family=Montserrat:wght@500;600;700&family=Open+Sans:wght@400;600&display=swap" rel="stylesheet">
<style>
:root{
  --bg:#d9d9d9;
  --ink:#1f1f1f;
  --dark:#2f2f2f;
  --panel:#4f4f4f;
  --rule:#3a3a3a;
  --paper:#ffffff;
}
*{box-sizing:border-box;margin:0;padding:0}
html,body{width:1200px;height:1200px;overflow:hidden;background:var(--bg)}
body{position:relative;font-family:"Open Sans",sans-serif;color:var(--ink)}
.page{position:absolute;top:238px;width:558px;height:722px;background:linear-gradient(#fff 70%,#efefef);overflow:hidden}
.page--front{left:32px}
.page--back{left:610px}
.hero{position:absolute;left:0;top:0;width:558px;height:254px;background:linear-gradient(180deg,#3a3a3a 0%,#232323 55%,#141414 100%)}
.hero-title{position:absolute;left:0;right:0;top:74px;text-align:center;font-family:Montserrat,sans-serif;font-weight:700;font-size:30px;color:#fff;letter-spacing:.3px}
.hero-tag{position:absolute;left:0;right:0;top:114px;display:flex;justify-content:center;align-items:center;gap:14px;font-family:Montserrat,sans-serif;font-weight:600;font-size:20px;color:#fff}
.hero-tag::before,.hero-tag::after{content:"";width:92px;height:2px;background:#fff}
.hero-quote{position:absolute;left:0;right:0;top:160px;text-align:center;font-family:Montserrat,sans-serif;font-weight:700;font-size:12.5px;color:#fff}
.lead{position:absolute;left:14px;right:16px;top:262px;font-size:11.6px;line-height:15.3px;text-align:justify}
.side{position:absolute;left:18px;top:320px;width:202px;height:318px;background:var(--panel);color:#fff;padding:16px 8px 0 10px}
.side h2{font-family:Montserrat,sans-serif;font-weight:600;margin-bottom:2px}
.side-about{font-size:16px}
.side-roi{font-size:13.5px}
.side p{font-size:8.5px;line-height:12px;letter-spacing:-.1px;text-align:justify}
.side hr{border:0;border-top:2px solid #bdbdbd;margin:14px 0 6px}
.block{position:absolute;left:230px;width:308px}
.block-head{border-top:2px solid var(--rule);padding-top:3px;height:24px;position:relative}
.block-head span{display:inline-block;background:var(--dark);color:#fff;font-family:Montserrat,sans-serif;font-weight:600;font-size:10.5px;padding:3px 18px 3px 4px;clip-path:polygon(0 0,100% 0,calc(100% - 8px) 100%,0 100%)}
.block-head i{display:inline-block;width:10px;height:19px;background:#5a5a5a;vertical-align:top;margin-left:-6px;clip-path:polygon(8px 0,100% 0,2px 100%,0 100%)}
.block p{font-size:8px;line-height:10.8px;text-align:justify;margin-top:8px}
.foot{position:absolute;left:0;bottom:0;width:558px;height:68px;background:linear-gradient(180deg,#5c5c5c,#3c3c3c);color:#fff;border-top:3px solid #222}
.foot-name{position:absolute;left:0;right:0;top:8px;text-align:center;font-family:Montserrat,sans-serif;font-weight:600;font-size:19px}
.foot-item{position:absolute;top:38px;display:flex;gap:5px;font-family:Montserrat,sans-serif;font-weight:600;font-size:7.4px;line-height:10px}
.foot-item svg{flex:none;margin-top:1px}
.foot-phone{letter-spacing:1.6px}
.back-bar{position:absolute;left:0;top:0;width:558px;height:61px;background:var(--dark);color:#fff;font-family:Montserrat,sans-serif;font-weight:700;font-size:29px;text-align:center;line-height:64px}
.back-band{position:absolute;left:0;top:64px;width:558px;height:13px;background:var(--dark)}
.grid{position:absolute;left:12px;top:99px;width:534px;display:grid;grid-template-columns:178px 180px 176px}
.col{border-right:1.5px solid var(--rule)}
.col:last-child{border-right:0}
.col-head{height:44px;background:var(--dark);color:#fff;font-family:Montserrat,sans-serif;font-weight:600;font-size:11.5px;line-height:14px;text-align:center;display:flex;align-items:center;justify-content:center;padding:0 6px}
.col ul{list-style:none;padding:20px 0 0 4px}
.col li{font-size:9.8px;line-height:13px;height:31.3px;padding-right:4px}
.col li::before{content:"• "}
.sub-head{height:44px;margin-top:6px;background:var(--dark);color:#fff;font-family:Montserrat,sans-serif;font-weight:600;font-size:12.5px;display:flex;align-items:center;justify-content:center}
.sub-list{padding-top:20px!important}
</style>
</head>
<body>

<section class="page page--front">
  <div class="hero" role="img" aria-label="Photograph of an executive boardroom table with chairs, in dark grey tones"></div>
  <h1 class="hero-title">DUN MERIDIAN SAFEGUARD</h1>
  <div class="hero-tag">EXPECT MORE</div>
  <p class="hero-quote">“INDUSTRY-LEADING PROTECTION FOR EXECUTIVE RISK.</p>

  <p class="lead">Meridian Safeguard is an exclusive, custom-designed insurance policy tailored to a company’s specific risk profile. The policy was created to provide clients with a premium, industry-leading level of protection not found in the standard insurance marketplace</p>

  <aside class="side">
    <h2 class="side-about">About us</h2>
    <p>Lorem ipsum dolor sit amet, consectetuer adipiscing elit. Aenean commodo ligula eget dolor. Aenean massa. Cum sociis natoque penatibus et magnis dis parturient montes, nascetur ridiculus mus.Lorem ipsum dolor sit amet, consectetuer adipiscing elit. Aenean commodo ligula eget dolor. Aenean massa. Cum sociis natoque penatibus et magnis dis parturient montes, nascetur ridiculus mus.</p>
    <hr>
    <h2 class="side-roi">Return on Investment</h2>
    <p>Lorem ipsum dolor sit amet, consectetuer adipiscing elit. Aenean commodo ligula eget dolor. Aenean massa. Cum sociis natoque penatibus et magnis dis parturient montes, nascetur ridiculus mus.Lorem ipsum dolor sit amet, consectetuer adipiscing elit. Aenean commodo ligula eget dolor. Aenean massa. Cum sociis natoque penatibus et magnis dis parturient montes, nascetur ridiculus mus.</p>
  </aside>

  <article class="block" style="top:326px">
    <div class="block-head"><span>Directors &amp; Officers Liability</span><i></i></div>
    <p>Lorem ipsum dolor sit amet, consectetuer adipiscing elit. Aenean commodo ligula eget dolor. Aenean massa. Cum sociis natoque penatibus et magnis dis parturient montes, nascetur ridiculus mus.Lorem ipsum dolor sit amet, consectetuer adipiscing elit. Aenean commodo ligula eget dolor. Aenean massa. Cum sociis natoque penatibus et magnis dis parturient montes, nascetur ridiculus mus.</p>
  </article>
  <article class="block" style="top:431px">
    <div class="block-head"><span>Employment Practices Liability</span><i></i></div>
    <p>Lorem ipsum dolor sit amet, consectetuer adipiscing elit. Aenean commodo ligula eget dolor. Aenean massa. Cum sociis natoque penatibus et magnis dis parturient montes, nascetur ridiculus mus.Lorem ipsum dolor sit amet, consectetuer adipiscing elit. Aenean commodo ligula eget dolor. Aenean massa. Cum sociis natoque penatibus et magnis dis parturient montes, nascetur ridiculus mus.</p>
  </article>
  <article class="block" style="top:538px">
    <div class="block-head"><span>Fiduciary Liability</span><i></i></div>
    <p>Lorem ipsum dolor sit amet, consectetuer adipiscing elit. Aenean commodo ligula eget dolor. Aenean massa. Cum sociis natoque penatibus et magnis dis parturient montes, nascetur ridiculus mus.Lorem ipsum dolor sit amet, consectetuer adipiscing elit. Aenean commodo ligula eget dolor. Aenean massa. Cum sociis natoque penatibus et magnis dis parturient montes, nascetur ridiculus mus.</p>
  </article>

  <footer class="foot" role="img" aria-label="Faded photograph of a business meeting behind the contact details">
    <div class="foot-name">CONTACT NAME</div>
    <div class="foot-item" style="left:18px"><svg width="7" height="9" viewBox="0 0 7 9"><path d="M3.5 0A3.3 3.3 0 0 0 .2 3.3C.2 5.6 3.5 9 3.5 9S6.8 5.6 6.8 3.3A3.3 3.3 0 0 0 3.5 0zm0 4.6a1.3 1.3 0 1 1 0-2.6 1.3 1.3 0 0 1 0 2.6z" fill="#fff"/></svg><span>Lorem ipsum dolor sit amet,<br>Lorem ipsum, 12345</span></div>
    <div class="foot-item foot-phone" style="left:228px"><svg width="7" height="7" viewBox="0 0 8 8"><path d="M1.6.2l1.3 1.9-.8.9c.5 1 1.4 1.9 2.4 2.4l.9-.8 1.9 1.3-.6 1.6C3.7 7.7.3 4.3.1.8z" fill="#fff"/></svg><span>555-014-2288<br>555-019-3377</span></div>
    <div class="foot-item" style="left:386px"><svg width="8" height="7" viewBox="0 0 8 6"><path d="M0 0h8v6H0z" fill="#fff"/><path d="M0 0l4 3.2L8 0" stroke="#555" stroke-width=".8" fill="none"/></svg><span>info@dunmeridiansafeguard.com</span></div>
  </footer>
</section>

<section class="page page--back">
  <div class="back-bar">COVERAGE HIGHLIGHTS</div>
  <div class="back-band"></div>

  <div class="grid">
    <div class="col">
      <div class="col-head">GENERAL TERMS &amp;<br>CONDITIONS</div>
      <ul>
        <li>This is one line of text that will be used in the</li>
        <li>This is one line of text that will be used in the</li>
        <li>This is one line of text that will be used in the</li>
        <li>This is one line of text that will be used in the</li>
        <li>This is one line of text that will be used in the</li>
        <li>This is one line of text that will be used in the</li>
        <li>This is one line of text that will be used in the</li>
        <li>This is one line of text that will be used in the</li>
        <li>This is one line of text that will be used in the</li>
        <li>This is one line of text that will be used in the</li>
        <li>This is one line of text that will be used in the</li>
        <li>This is one line of text that will be used in the</li>
        <li>This is one line of text that will be used in the</li>
        <li>This is one line of text that will be used in the</li>
        <li>This is one line of text that will be used in the</li>
      </ul>
    </div>
    <div class="col">
      <div class="col-head">DIRECTORS &amp; OFFICERS<br>LIABILITY</div>
      <ul>
        <li>This is one line of text that will be used in the</li>
        <li>This is one line of text that will be used in the</li>
        <li>This is one line of text that will be used in the</li>
        <li>This is one line of text that will be used in the</li>
        <li>This is one line of text that will be used in the</li>
        <li>This is one line of text that will be used in the</li>
        <li>This is one line of text that will be used in the</li>
        <li>This is one line of text that will be used in the</li>
        <li>This is one line of text that will be used in the</li>
        <li>This is one line of text that will be used in the</li>
        <li>This is one line of text that will be used in the</li>
        <li>This is one line of text that will be used in the</li>
        <li>This is one line of text that will be used in the</li>
        <li>This is one line of text that will be used in the</li>
        <li>This is one line of text that will be used in the</li>
      </ul>
    </div>
    <div class="col">
      <div class="col-head">EMPLOYMENT<br>PRACTICES LIABILITY</div>
      <ul>
        <li>This is one line of text that will be used in the</li>
        <li>This is one line of text that will be used in the</li>
        <li>This is one line of text that will be used in the</li>
        <li>This is one line of text that will be used in the</li>
        <li>This is one line of text that will be used in the</li>
      </ul>
      <div class="sub-head">FIDUCIARY LIABILITY</div>
      <ul class="sub-list">
        <li>This is one line of text that will be used in the</li>
        <li>This is one line of text that will be used in the</li>
        <li>This is one line of text that will be used in the</li>
        <li>This is one line of text that will be used in the</li>
        <li>This is one line of text that will be used in the</li>
        <li>This is one line of text that will be used in the</li>
        <li>This is one line of text that will be used in the</li>
        <li>This is one line of text that will be used in the</li>
      </ul>
    </div>
  </div>

  <footer class="foot" role="img" aria-label="Faded photograph of a business meeting behind the contact details">
    <div class="foot-name">CONTACT NAME</div>
    <div class="foot-item" style="left:22px"><svg width="7" height="9" viewBox="0 0 7 9"><path d="M3.5 0A3.3 3.3 0 0 0 .2 3.3C.2 5.6 3.5 9 3.5 9S6.8 5.6 6.8 3.3A3.3 3.3 0 0 0 3.5 0zm0 4.6a1.3 1.3 0 1 1 0-2.6 1.3 1.3 0 0 1 0 2.6z" fill="#fff"/></svg><span>Lorem ipsum dolor sit amet,<br>Lorem ipsum, 12345</span></div>
    <div class="foot-item foot-phone" style="left:228px"><svg width="7" height="7" viewBox="0 0 8 8"><path d="M1.6.2l1.3 1.9-.8.9c.5 1 1.4 1.9 2.4 2.4l.9-.8 1.9 1.3-.6 1.6C3.7 7.7.3 4.3.1.8z" fill="#fff"/></svg><span>555-014-2288<br>555-019-3377</span></div>
    <div class="foot-item" style="left:386px"><svg width="8" height="7" viewBox="0 0 8 6"><path d="M0 0h8v6H0z" fill="#fff"/><path d="M0 0l4 3.2L8 0" stroke="#555" stroke-width=".8" fill="none"/></svg><span>info@dunmeridiansafeguard.com</span></div>
  </footer>
</section>

</body>
</html>
```